Website Re-design for Kids Playhouse Business

Need current website which looks very outdated to be re-designed to look modern and contemporary, reduce clutter significantly and make it look elegant and simple.
Current website: http://www.tamblewood.com.au/
A website which the business owner likes, use as reference/inspiration: http://rivesta.com.au/
Looking for light green palette, natural colours. "WHAT'S ON" page/link no longer required.
Updates
Industry/Entity Type
Business
Number of Pages Required
5+ page
Look and feel

```html
<!DOCTYPE html>
<html lang="en">
<head>
<meta charset="utf-8">
<title>Tamblewood Kids Playhouse &amp; Cafe</title>
<link rel="stylesheet" href="https://fonts.googleapis.com/css2?family=Fredoka:wght@500;600&family=Montserrat:wght@400;600;700&family=Playfair+Display:ital,wght@1,600&display=swap">
<style>
:root{
  --green:#3fb64a;
  --green-soft:#52c05b;
  --green-dark:#2f9a3a;
  --yellow:#fff200;
  --yellow-btn:#f5ea14;
  --grey-bg:#e4e4e4;
  --grey-text:#6d6d6d;
  --ink:#3a3a3a;
  --mint:#eafcd3;
  --card:#d9dccd;
  --white:#ffffff;
}
*{margin:0;padding:0;box-sizing:border-box}
html,body{width:1200px;height:3355px;overflow:hidden}
body{position:relative;font-family:"Montserrat",sans-serif;color:var(--ink);background:var(--white)}
.abs{position:absolute}
.btn{position:absolute;background:var(--yellow-btn);color:var(--green-dark);font-family:"Montserrat",sans-serif;font-weight:700;text-transform:uppercase;font-size:12px;display:flex;align-items:center;justify-content:center;border-radius:2px}

/* hero */
.hero{left:0;top:0;width:1200px;height:555px;background:linear-gradient(180deg,#9c8a78 0%,#c7a98a 40%,#8a6f5a 100%)}
.hero-photo{left:0;top:0;width:1200px;height:555px;background:radial-gradient(ellipse at 30% 40%,#e6c9a8 0%,rgba(230,201,168,0) 45%),radial-gradient(ellipse at 68% 45%,#e9caa5 0%,rgba(233,202,165,0) 40%),linear-gradient(180deg,#7f93a3 0%,#b8977a 55%,#6e5f54 100%)}
.menu-icon{left:118px;top:42px}
.brand{left:172px;top:38px;width:140px;height:120px;display:flex;flex-direction:column;align-items:center;justify-content:center;font-family:"Fredoka",sans-serif;font-weight:600;color:var(--yellow);font-size:38px;line-height:1;text-align:center}
.eclub{left:790px;top:42px;width:138px;height:32px;font-size:14px;text-transform:none;color:var(--green-dark)}
.call{left:938px;top:42px;height:32px;display:flex;align-items:center;color:var(--white);font-weight:700;font-size:15px}
.hero-title{left:0;top:282px;width:1200px;text-align:center;font-family:"Playfair Display",serif;font-style:italic;font-weight:600;font-size:58px;color:var(--white)}

/* about */
.about{left:0;top:555px;width:1200px;height:463px;background:var(--grey-bg)}
.about-ring{left:103px;top:604px;width:374px;height:374px;border-radius:50%;background:var(--yellow)}
.about-photo{left:121px;top:622px;width:338px;height:338px;border-radius:50%;background:linear-gradient(135deg,#cfe3f1 0%,#e8c4a6 45%,#5fa3d6 100%)}
.about-title{left:510px;top:676px;font-family:"Fredoka",sans-serif;font-weight:600;font-size:24px;color:var(--green)}
.about-sub{left:510px;top:716px;font-weight:700;font-size:15px;color:#8a8a8a}
.about-text{left:510px;top:750px;width:570px;font-size:13px;line-height:22px;color:var(--grey-text)}
.read-more{left:513px;top:882px;width:102px;height:30px;font-size:10px}

/* features */
.features{left:0;top:1018px;width:1200px;height:695px;background:var(--green-soft)}
.features-bg{left:0;top:1018px;width:1200px;height:695px;background:radial-gradient(ellipse at 60% 30%,rgba(255,255,255,.12) 0%,rgba(255,255,255,0) 50%),radial-gradient(ellipse at 20% 80%,rgba(0,0,0,.06) 0%,rgba(0,0,0,0) 50%)}
.section-title{left:0;width:1200px;text-align:center;font-family:"Fredoka",sans-serif;font-weight:600;font-size:34px;line-height:42px}
.feature-photo{width:340px;height:340px;border-radius:50%;top:1145px}
.feature-caption{width:340px;top:1502px;text-align:center;color:var(--white);font-family:"Fredoka",sans-serif;font-weight:600;font-size:19px;line-height:24px}
.feature-btn{width:142px;height:30px;top:1575px;font-size:11px}
.dots{display:flex;gap:6px}
.dot{width:14px;height:14px;border-radius:50%;background:var(--white)}
.dot.muted{background:#9fdca4}

/* testimonials */
.testimonials{left:0;top:1713px;width:1200px;height:478px;background:linear-gradient(180deg,#d4d4d4 0%,#e6e6e6 50%,#cfcfcf 100%)}
.avatar{left:546px;top:1838px;width:108px;height:108px;border-radius:50%;background:linear-gradient(160deg,#c98a5a 0%,#f0c9a8 60%,#e6b38d 100%);border:3px solid var(--white)}
.quote{left:250px;top:1962px;width:700px;text-align:center;font-size:18px;line-height:29px;color:#444}
.quote-name{left:0;top:2064px;width:1200px;text-align:center;font-weight:700;font-size:13px;color:#444}

/* contact */
.contact{left:0;top:2191px;width:1200px;height:538px;background:var(--mint)}
.info-card{left:120px;width:363px;height:123px;background:var(--card);border-radius:4px;text-align:center;padding-top:40px}
.info-card h3{font-family:"Fredoka",sans-serif;font-weight:600;font-size:16px;color:var(--green);margin-bottom:8px}
.info-card p{font-size:14px;line-height:21px;color:#555}
.field{background:var(--mint);border:2px solid #cfe6b5;border-radius:6px;font-size:14px;color:#888;padding:0 18px;display:flex;align-items:center}
.send{left:520px;top:2606px;width:145px;height:40px;font-size:15px;text-transform:none}

/* footer */
.footer{left:0;top:2729px;width:1200px;height:626px;background:var(--green)}
.footer-bg{left:0;top:2729px;width:1200px;height:626px;background:radial-gradient(ellipse at 50% 80%,rgba(0,0,0,.1) 0%,rgba(0,0,0,0) 55%),radial-gradient(ellipse at 80% 20%,rgba(255,255,255,.08) 0%,rgba(255,255,255,0) 45%)}
.footer-col{top:2778px;width:307px;height:292px;border:2px solid rgba(255,255,255,.7);border-radius:10px;padding:22px 26px;color:var(--white)}
.footer-col h4{font-weight:700;font-size:15px;text-transform:uppercase;margin-bottom:14px}
.footer-col p{font-size:11.5px;line-height:19px}
.footer-col ul{list-style:none}
.footer-col li{font-size:11.5px;line-height:16px;margin-bottom:10px;padding-left:18px;position:relative}
.footer-col li::before{content:"";position:absolute;left:0;top:3px;width:9px;height:9px;border-radius:50%;background:rgba(255,255,255,.75)}
.footer-col .btn{position:static;width:140px;height:28px;font-size:10px;margin-top:16px}
.footer-brand{left:0;top:3128px;width:1200px;text-align:center;color:var(--white);font-family:"Fredoka",sans-serif;font-weight:600;font-size:34px;line-height:38px}
.footer-brand small{display:block;font-size:22px;line-height:26px}
.social{left:562px;top:3220px;display:flex;gap:14px}
.social span{width:30px;height:30px;border-radius:50%;border:3px solid var(--white)}
.copyright{left:0;top:3297px;width:1200px;text-align:center;color:var(--white);font-size:11px;font-weight:600}
</style>
</head>
<body>

<!-- hero -->
<div class="abs hero"></div>
<div class="abs hero-photo" role="img" aria-label="Smiling children sitting at a classroom table with pencils and a globe"></div>
<svg class="abs menu-icon" width="30" height="26" viewBox="0 0 30 26"><rect y="0" width="30" height="4" fill="#3fb64a"/><rect y="10" width="30" height="4" fill="#3fb64a"/><rect y="20" width="30" height="4" fill="#3fb64a"/></svg>
<div class="abs brand">Tamble<br>wood<br>Kids</div>
<div class="btn eclub">Join Our E-club</div>
<div class="abs call">Call: 02 9000 0100</div>
<h1 class="abs hero-title">So much fun for everyone</h1>

<!-- about -->
<section class="abs about"></section>
<div class="abs about-ring"></div>
<div class="abs about-photo" role="img" aria-label="Mother and two young children painting together at a table"></div>
<h2 class="abs about-title">ABOUT TAMBLEWOOD KIDS PLAYHOUSE &amp; CAFE</h2>
<p class="abs about-sub">Welcome to Tamblewood Kids, Sydney's newest and best party &amp; play centre!</p>
<p class="abs about-text">Tamblewood Kids is an Indoor Kids Play Centre and Cafe that offers both kids and adults a chance to enjoy their time, together! We pride ourselves in offering the best indoor play centre for your kids to engage in fun and learning activities in a specially created environment that is not only warm and safe but also enhances and stimulates creativity and curiosity in a child. Tamblewood Kids offers a variety of kids party venues like our themed party rooms which are hand painted.</p>
<div class="btn read-more">Read More</div>

<!-- features -->
<section class="abs features"></section>
<div class="abs features-bg" role="img" aria-label="Faded photo of children playing behind a green tint"></div>
<h2 class="abs section-title" style="top:1064px;color:var(--white)">Our Features</h2>

<div class="abs feature-photo" style="left:75px;background:linear-gradient(150deg,#4a3a32 0%,#b07a55 50%,#e0a560 100%)" role="img" aria-label="Family celebrating a birthday with a large cake"></div>
<div class="abs feature-photo" style="left:429px;background:linear-gradient(150deg,#6a3a7a 0%,#d86aa0 50%,#f0b0c0 100%)" role="img" aria-label="Decorated party room with balloons and a costumed host"></div>
<div class="abs feature-photo" style="left:785px;background:linear-gradient(150deg,#e03a3a 0%,#f5d63a 50%,#b82a3a 100%)" role="img" aria-label="Costumed characters at a school holiday program"></div>

<div class="abs feature-caption" style="left:75px">Perfect venue for<br>birthdays and private parties</div>
<div class="abs feature-caption" style="left:429px">4 kids loving<br>party rooms themes</div>
<div class="abs feature-caption" style="left:785px">We host school<br>holiday programs</div>

<div class="btn feature-btn" style="left:174px">View Parties</div>
<div class="btn feature-btn" style="left:528px">View Party Rooms</div>
<div class="btn feature-btn" style="left:884px">View Programs</div>

<div class="abs dots" style="left:572px;top:1662px"><span class="dot muted"></span><span class="dot"></span><span class="dot"></span></div>

<!-- testimonials -->
<section class="abs testimonials" role="img" aria-label="Grey chalkboard background with faint children's chalk drawings"></section>
<h2 class="abs section-title" style="top:1760px;color:var(--green)">What People Say About Us</h2>
<div class="abs avatar" role="img" aria-label="Portrait of the reviewer"></div>
<p class="abs quote">Had my son's birthday party there. Kids had such a great time I recommend this place to everyone.Staff are amazing. Food and coffee are delicious! Thank you</p>
<p class="abs quote-name">Dana Whitfield</p>
<div class="abs dots" style="left:572px;top:2131px"><span class="dot" style="background:#5cc563"></span><span class="dot"></span><span class="dot"></span></div>

<!-- contact -->
<section class="abs contact"></section>
<h2 class="abs section-title" style="top:2244px;color:var(--green)">Contact Us</h2>

<div class="abs info-card" style="top:2331px">
  <h3>Postal Address</h3>
  <p>14 Willow Street Greenvale 2190<br>NSW Australia.</p>
</div>
<svg class="abs" width="48" height="70" viewBox="0 0 48 70" style="left:277px;top:2284px">
  <path d="M24 4C13 4 5 12 5 23c0 14 19 37 19 37s19-23 19-37C43 12 35 4 24 4z" fill="none" stroke="#3fb64a" stroke-width="5"/>
  <circle cx="24" cy="23" r="7" fill="none" stroke="#3fb64a" stroke-width="5"/>
  <ellipse cx="24" cy="64" rx="14" ry="4" fill="#3fb64a"/>
</svg>

<div class="abs info-card" style="top:2522px">
  <h3>Phone &amp; E-mail</h3>
  <p>Ph: 02 9000 0100 | Fax: 02 9000 0199<br>Email: hello@tamblewoodkids.com.au</p>
</div>
<svg class="abs" width="70" height="64" viewBox="0 0 70 64" style="left:266px;top:2480px">
  <circle cx="35" cy="32" r="27" fill="none" stroke="#3fb64a" stroke-width="5"/>
  <path d="M24 18c-4 3-5 8-2 14 4 8 10 14 17 16 4 1 7-1 9-4l-7-6-4 3c-4-2-8-6-10-10l3-4z" fill="#3fb64a"/>
</svg>

<div class="abs field" style="left:520px;top:2329px;width:270px;height:44px">Your Name</div>
<div class="abs field" style="left:800px;top:2329px;width:270px;height:44px">Phone</div>
<div class="abs field" style="left:520px;top:2390px;width:270px;height:44px">Your Email</div>
<div class="abs field" style="left:800px;top:2390px;width:270px;height:44px">Postcode</div>
<div class="abs field" style="left:520px;top:2451px;width:550px;height:136px;align-items:flex-start;padding-top:12px">Your Message</div>
<div class="btn send">Send Message</div>

<!-- footer -->
<footer class="abs footer"></footer>
<div class="abs footer-bg" role="img" aria-label="Faded photo of children in the play area behind a green tint"></div>

<div class="abs footer-col" style="left:120px">
  <h4>About Us</h4>
  <p>We welcome all the kids to come and play at our Greenvale indoor play centre. Our kids play centre features slides and lots of other fun activities. We also have a safe toddler area, while you enjoy a cup of coffee and cake, or some lunch from our extensive cafe menu where we only use the freshest "A" grade quality ingredients.</p>
  <div class="btn">Join Our E-club</div>
</div>
<div class="abs footer-col" style="left:447px">
  <h4>Our Features</h4>
  <ul>
    <li>Ball pit</li>
    <li>Safe baby play area for 12 to 24 months</li>
    <li>4 x lane slim side</li>
    <li>Rock climbing</li>
    <li>Toddler &amp; younger kids play area for 2 to 5 years</li>
  </ul>
</div>
<div class="abs footer-col" style="left:773px">
  <h4>Greenvale Latest Posts</h4>
  <p>No Recent Post available</p>
</div>

<div class="abs footer-brand">TAMBLEWOOD KIDS<small>Playhouse &amp; Cafe</small></div>
<div class="abs social"><span></span><span></span></div>
<p class="abs copyright">SITE CONTENTS © 2018 WWW.TAMBLEWOOD.COM.AU</p>

</body>
</html>
```